Re-design a highly converting profile page for my website

My website allows people to book a mentor for long-term mentorship as well as sessions. I would like to re-design this site within our branding guidelines to give people the best profile possible.

Please give this website a modern look and concentrate on the CTA and conversion rates. This is a highly converting site and it should stay that way or even get better!

Please also keep menu bar & footer in tact

Target Market(s)

Developers, Designers, Entrepreneurs in the Tech industry

Number of Pages Required

1 page

Requirements
Must have
• Strong CTA, existing color palette, testimonials and major elements
Nice to have
• Modern look, easy to see CTA, easy to scan offer. Not too crowded
Should not have
• No reporpusing. It is and stays a profile page

```html
<!DOCTYPE html>
<html lang="en">
<head>
<meta charset="utf-8">
<title>Jordan Ellery – Mentor Profile</title>
<link href="https://fonts.googleapis.com/css2?family=Montserrat:wght@400;500;600;700&display=swap" rel="stylesheet">
<style>
:root{
  --bg:#f8f8f8;
  --ink:#2e2e33;
  --muted:#666;
  --teal:#00cfb4;
  --cyan:#10d3e0;
  --gold:#f8b922;
  --band:#e4e4e4;
  --arc:#ececec;
}
*{margin:0;padding:0;box-sizing:border-box}
html,body{width:1200px;height:1023px;overflow:hidden;background:var(--bg)}
body{font-family:'Montserrat',sans-serif;color:var(--ink);position:relative}
.arcs{position:absolute;inset:0;width:1200px;height:1023px}
.brand{position:absolute;left:66px;top:48px;display:flex;align-items:center;gap:10px}
.brand-dot{width:60px;height:60px;border-radius:50%;background:var(--teal)}
.brand-name{font-weight:700;font-size:18px;color:var(--ink)}
.nav a{position:absolute;top:70px;font-size:13px;font-weight:500;color:var(--ink);text-decoration:none}
.nav .star{position:absolute;left:832px;top:64px;font-size:18px}
.btn-login,.btn-start{position:absolute;top:58px;width:123px;height:37px;border-radius:19px;color:#fff;font-size:13px;font-weight:600;display:flex;align-items:center;justify-content:center}
.btn-login{left:871px;background:linear-gradient(90deg,var(--teal),var(--cyan))}
.btn-start{left:1007px;background:var(--ink)}
.country{position:absolute;left:66px;top:253px;height:26px;padding:0 11px;background:var(--ink);color:#fff;font-size:15.5px;font-weight:500;letter-spacing:1.6px;line-height:26px;box-shadow:2px 2px 4px rgba(0,0,0,.2)}
.name{position:absolute;left:64px;top:282px;font-size:66px;font-weight:600;letter-spacing:-1px;text-shadow:3px 3px 0 var(--teal)}
.role{position:absolute;left:63px;top:358px;font-size:23.5px;font-weight:500}
.rating{position:absolute;left:64px;top:398px;display:flex;align-items:center;gap:18px}
.stars{color:var(--gold);font-size:30px;letter-spacing:2px}
.score{font-size:18px;font-weight:500}
.score span{color:#aaa}
.bio{position:absolute;left:63px;top:450px;width:430px;font-size:12.8px;line-height:16.8px;color:#444}
.btn-book{position:absolute;left:66px;top:597px;width:202px;height:53px;border-radius:22px;background:var(--ink);color:#fff;font-size:18px;font-weight:500;display:flex;align-items:center;justify-content:center;box-shadow:2px 4px 0 var(--teal)}
.social-label{position:absolute;left:280px;top:605px;font-size:11.5px;font-weight:700;line-height:19px}
.social-label b{display:block;border-bottom:2px solid var(--gold);font-weight:700}
.social-icons{position:absolute;left:342px;top:614px;display:flex;gap:16px}
.social-icons i{width:16px;height:16px;border-radius:50%;background:#9a9a9a;display:block}
.portrait{position:absolute;left:655px;top:216px}
.photo{position:absolute;left:714px;top:274px;width:360px;height:360px;border-radius:50%;background:linear-gradient(180deg,#8a5a3e 0%,#e3b497 32%,#e6b094 58%,#e8867f 80%,#e37876 100%)}
.band{position:absolute;left:0;top:768px;width:1200px;height:210px;background:var(--band)}
.svc-title{position:absolute;left:68px;top:828px;font-size:30px;font-weight:700}
.svc-title span{color:var(--gold)}
.svc-sub{position:absolute;left:68px;top:874px;font-size:15.5px;line-height:19px;color:#555}
.num{position:absolute;font-size:31px;font-weight:600}
.svc-name{position:absolute;font-size:24px;font-weight:700;line-height:29px}
.card{position:absolute;left:686px;top:738px;width:240px;height:238px;background:var(--gold);box-shadow:0 3px 8px rgba(0,0,0,.15)}
.card .icon{position:absolute;left:132px;top:-10px;width:92px;height:92px;border-radius:8px;background:#d99a10}
.card .num{left:25px;top:50px}
.card .svc-name{left:25px;top:126px}
.card p{position:absolute;left:25px;top:176px;width:190px;font-size:11px;line-height:13.6px;color:#4a3a10}
.next{position:absolute;left:1132px;top:857px}
</style>
</head>
<body>
<svg class="arcs" viewBox="0 0 1200 1023" aria-hidden="true">
  <circle cx="-10" cy="400" r="220" fill="none" stroke="var(--arc)" stroke-width="60"/>
  <circle cx="1260" cy="260" r="230" fill="none" stroke="var(--arc)" stroke-width="50"/>
</svg>

<header>
  <div class="brand"><span class="brand-dot"></span><span class="brand-name">Keelway</span></div>
  <nav class="nav">
    <a style="left:486px">Find a Mentor</a>
    <a style="left:604px">For Businesses</a>
    <a style="left:726px">Book a Session</a>
    <span class="star">★</span>
  </nav>
  <div class="btn-login">Login</div>
  <div class="btn-start">Get Started</div>
</header>

<section class="profile">
  <div class="country">UNITED STATES OF AMERICA</div>
  <h1 class="name">Jordan Ellery</h1>
  <div class="role">Director of Product - Harbor Mutual</div>
  <div class="rating"><span class="stars">★★★★★</span><span class="score">5.0 <span>(7 reviews)</span></span></div>
  <p class="bio">Jordan is currently the Director of Product at Harbor Mutual (www.harbormutual.example). He was previously the CPO of Lumen Story Labs (www.lumenstory.example) which operated in the AdTech industry, helping the world's largest media companies with data-inspired storytelling. Previously a Senior Product leader at Northbound Trips (www.northbound.example) and Printwell Digital (www.printwell.example/digital)</p>
  <div class="btn-book">Book a Session</div>
  <div class="social-label"><b>SOCIAL</b>MEDIA</div>
  <div class="social-icons"><i></i><i></i><i></i></div>

  <svg class="portrait" width="478" height="478" viewBox="0 0 478 478" aria-hidden="true">
    <circle cx="239" cy="238" r="210" fill="none" stroke="var(--teal)" stroke-width="56"/>
  </svg>
  <div class="photo" role="img" aria-label="Portrait photo of the mentor smiling, wearing a coral shirt"></div>
</section>

<section class="band"></section>
<h2 class="svc-title">Available <span>Services</span></h2>
<p class="svc-sub">Gain access to personalized<br>guidance to reach your potential</p>

<div class="num" style="left:477px;top:826px">01.</div>
<div class="svc-name" style="left:477px;top:896px">Personal Chat</div>

<div class="card">
  <div class="icon" role="img" aria-label="Notebook and pencil icon"></div>
  <div class="num">02.</div>
  <div class="svc-name">To-Dos &amp; Goals</div>
  <p>Unlimited access to the mentor via chat, e-mail or text, within reason.</p>
</div>

<div class="num" style="left:960px;top:806px">03.</div>
<div class="svc-name" style="left:960px;top:882px">Challenges<br>&amp; Projects</div>

<svg class="next" width="42" height="42" viewBox="0 0 42 42" aria-label="Next service">
  <circle cx="21" cy="21" r="19" fill="none" stroke="var(--gold)" stroke-width="2.5"/>
  <path d="M18 13 L26 21 L18 29" fill="none" stroke="var(--gold)" stroke-width="2.5" stroke-linecap="round"/>
</svg>
</body>
</html>
```